Business cards, stationary & real estate signs
LT&R Design
Business cards, stationary & real estate signs -
Creative Brief
Bright & Fun-filled
Joan V. Marsh
Broker, Realtor, CSP
4821 Tindall Lane, Suite 118 Brookmere, ST 00417
joan@gretaholmvale.example
www.joan.quadranthousefinder.example
In addition to business card and stationary we would also like a design for our real estate signs using the colors on our logo. The signs will be mounted to posts and will be 30x24in

```html
<!DOCTYPE html>
<html lang="en">
<head>
<meta charset="utf-8">
<title>LT&amp;R Design – Business Cards</title>
<link rel="stylesheet" href="https://fonts.googleapis.com/css2?family=Open+Sans:wght@400;600;700;800&display=swap">
<style>
  :root {
    --backdrop: #e9e4dc;
    --card-white: #ffffff;
    --brand-blue: #1a74ad;
    --brand-blue-deep: #0e5a8e;
    --brand-green: #a8cf2f;
    --brand-green-light: #bcdc4a;
    --ink: #222222;
    --ink-soft: #444444;
    --divider: #a8cf2f;
  }
  * { box-sizing: border-box; margin: 0; padding: 0; }
  html, body { width: 1200px; height: 751px; overflow: hidden; }
  body {
    position: relative;
    background: var(--backdrop);
    font-family: "Open Sans", Arial, sans-serif;
  }
  .card {
    position: absolute;
    border-radius: 26px;
    overflow: hidden;
    box-shadow: 0 4px 14px rgba(0,0,0,0.18);
  }
  /* Front card */
  .card-front {
    left: 360px; top: 80px; width: 482px; height: 316px;
    background: var(--card-white);
  }
  .card-front .wordmark {
    position: absolute; left: 22px; top: 138px;
    font-size: 66px; font-weight: 800; letter-spacing: -2px; line-height: 1;
    color: var(--brand-blue);
  }
  .card-front .divider {
    position: absolute; left: 236px; top: 46px;
    width: 1px; height: 200px; background: var(--divider);
  }
  .card-front .details {
    position: absolute; right: 22px; top: 50px; width: 215px;
    text-align: right;
    color: var(--ink); font-size: 11px; line-height: 1.35;
  }
  .details .name { font-size: 18px; font-weight: 700; line-height: 1.2; }
  .details .title { font-size: 11px; font-weight: 600; color: var(--ink-soft); }
  .details .address { margin-top: 50px; }
  .details .phones { margin-top: 24px; }
  .details .phones p + p { margin-top: 14px; }
  .details .email { margin-top: 16px; white-space: nowrap; }
  .card-front .band-blue {
    position: absolute; left: 0; right: 0; bottom: 24px; height: 5px;
    background: var(--brand-blue);
  }
  .card-front .band-green {
    position: absolute; left: 0; right: 0; bottom: 0; height: 20px;
    background: var(--brand-green);
  }
  /* Back cards */
  .card-back { top: 439px; width: 548px; height: 210px; }
  .card-back-blue {
    left: 48px;
    background: linear-gradient(135deg, var(--brand-blue) 0%, var(--brand-blue-deep) 100%);
  }
  .card-back-green {
    left: 607px;
    background: linear-gradient(135deg, var(--brand-green-light) 0%, var(--brand-green) 100%);
  }
  .card-back .wordmark {
    position: absolute; left: 0; right: 0; top: 64px;
    text-align: center;
    font-size: 96px; font-weight: 800; letter-spacing: -3px; line-height: 1;
  }
  .card-back-blue .wordmark { color: #ffffff; }
  .card-back-green .wordmark { color: var(--brand-blue); }
  .card-back .website {
    position: absolute; left: 0; right: 0; bottom: 12px;
    text-align: center;
    font-size: 10.5px;
  }
  .card-back-blue .website { color: #ffffff; }
  .card-back-green .website { color: var(--ink-soft); }
</style>
</head>
<body>

  <section class="card card-front" aria-label="Business card front">
    <div class="wordmark">LT&amp;R</div>
    <div class="divider"></div>
    <div class="details">
      <p class="name">Joan V. Marsh</p>
      <p class="title">Broker, Realtor, CSP</p>
      <p class="address">4821 Tindall Lane, Suite 118<br>Brookmere, ST 00417</p>
      <div class="phones">
        <p>Phone: 555-204-3816</p>
        <p>Fax: 555-204-3817</p>
      </div>
      <p class="email">Email: joan@gretaholmvale.example</p>
    </div>
    <div class="band-blue"></div>
    <div class="band-green"></div>
  </section>

  <section class="card card-back card-back-blue" aria-label="Business card back, blue">
    <div class="wordmark">LT&amp;R</div>
    <p class="website">www.joan.quadranthousefinder.example</p>
  </section>

  <section class="card card-back card-back-green" aria-label="Business card back, green">
    <div class="wordmark">LT&amp;R</div>
    <p class="website">www.joan.quadranthousefinder.example</p>
  </section>

</body>
</html>
```